Crestline Lending Group Business Cards

We are looking to revamp the current business cards each of our locations uses. We are a lending company that specializes in personal loans, title loans, and tax services. We have locations in New Mexico, Texas, and Oklahoma.

We would like a cleaner, sleeker look while still highlighting what we offer. Title Loans, Personal Loans & Tax Services. We also want to include our referral fee somewhere on the card. We would like to see an English option as well as a Spanish option for the cards.

PLEASE NOTE: Some business cards do not include the employee's name but just the store's location, while others will include both.

These are double-sided business cards, and we would like to see proof if possible. I have included proofs of our current business cards for you to review below, as well as our company logo. Feel free to get creative with the logo, etc! Colors should match the logo; however, you do not need to use all of our logo colors if you don't want to.

```html
<!DOCTYPE html>
<html lang="en">
<head>
<meta charset="utf-8">
<title>Crestline Lending Group – Business Card</title>
<link rel="stylesheet" href="https://fonts.googleapis.com/css2?family=Montserrat:wght@300;400;600;700;800&family=Poppins:wght@400;700;800&display=swap">
<style>
  :root{
    --backdrop:#3b3b3b;
    --paper:#ffffff;
    --brand-green:#11502e;
    --brand-red:#c41e26;
    --ink:#111111;
    --muted:#6b6b6b;
    --photo-light:#e9ecee;
    --photo-mid:#c9d1cf;
  }
  *{margin:0;padding:0;box-sizing:border-box}
  html,body{width:972px;height:1200px;overflow:hidden;background:var(--backdrop)}
  body{position:relative;font-family:"Montserrat",sans-serif}

  .card{position:absolute;left:113px;width:747px;height:426px;background:var(--paper);overflow:hidden}
  .card--front{top:117px}
  .card--back{top:659px}

  /* front */
  .brand-name{position:absolute;left:40px;top:108px;width:300px;text-align:center;
    color:var(--brand-green);font-weight:700;font-size:27px;line-height:1.15;letter-spacing:-.3px}
  .divider{position:absolute;left:354px;top:63px;width:4px;height:171px;background:var(--brand-red)}
  .contact{position:absolute;left:389px;top:82px;color:var(--ink)}
  .contact__name{font-weight:800;font-size:31px;line-height:1;letter-spacing:-.5px}
  .contact__role{margin-top:6px;font-weight:300;font-size:16px;color:var(--muted)}
  .contact__phone{margin-top:8px;margin-left:-4px;font-weight:800;font-size:35px;line-height:1;letter-spacing:-.3px}
  .contact__email{margin-top:8px;font-weight:300;font-size:16px;color:var(--muted)}

  .services{position:absolute;left:0;top:273px;width:100%;height:96px;background:var(--brand-green);
    display:flex;align-items:center;justify-content:center;gap:48px;list-style:none}
  .service{display:flex;align-items:center;gap:8px;color:var(--paper);font-weight:600;font-size:21px}
  .service svg{width:26px;height:26px;flex:none}
  .address{position:absolute;left:0;top:369px;width:100%;height:57px;display:flex;align-items:center;justify-content:center;
    font-weight:700;font-size:21px;color:var(--ink);letter-spacing:-.2px}

  /* back */
  .referral-panel{position:absolute;left:0;top:0;width:371px;height:100%;background:var(--brand-red)}
  .gift-photo{position:absolute;left:240px;top:60px;width:450px;height:300px;border-radius:6px;
    background:linear-gradient(90deg,rgba(140,20,26,.55) 0%,rgba(140,20,26,.35) 28%,var(--photo-mid) 30%,var(--photo-light) 70%,var(--paper) 100%)}
  .ribbon{position:absolute;left:0;top:0;width:371px;height:426px}
  .offer{position:absolute;left:67px;top:158px;color:var(--paper);font-family:"Poppins",sans-serif}
  .offer__lead{display:flex;align-items:center;gap:10px}
  .offer__get{font-weight:800;font-size:38px;line-height:1;letter-spacing:-1px}
  .offer__upto{background:var(--brand-green);font-weight:400;font-size:23px;line-height:28px;padding:0 12px}
  .offer__amount{font-weight:800;font-size:100px;line-height:1;letter-spacing:-6px;margin-top:-2px}
</style>
</head>
<body>
  <section class="card card--front">
    <div class="brand-name">Crestline<br>Lending Group</div>
    <div class="divider"></div>
    <div class="contact">
      <div class="contact__name">Maria Reyes</div>
      <div class="contact__role">Branch Manager</div>
      <div class="contact__phone">(505) 555-0148</div>
      <div class="contact__email">info@crestlinelending.com</div>
    </div>
    <ul class="services">
      <li class="service"><svg viewBox="0 0 26 26"><circle cx="13" cy="13" r="13" fill="#fff"/><path d="M7.5 13.5l4 4 7-8" fill="none" stroke="#11502e" stroke-width="2.6" stroke-linecap="round" stroke-linejoin="round"/></svg>Title loans</li>
      <li class="service"><svg viewBox="0 0 26 26"><circle cx="13" cy="13" r="13" fill="#fff"/><path d="M7.5 13.5l4 4 7-8" fill="none" stroke="#11502e" stroke-width="2.6" stroke-linecap="round" stroke-linejoin="round"/></svg>Personal Loans</li>
      <li class="service"><svg viewBox="0 0 26 26"><circle cx="13" cy="13" r="13" fill="#fff"/><path d="M7.5 13.5l4 4 7-8" fill="none" stroke="#11502e" stroke-width="2.6" stroke-linecap="round" stroke-linejoin="round"/></svg>Tax Services</li>
    </ul>
    <div class="address">456 Oak Avenue, Suite B, Riverton, Texas 55555</div>
  </section>

  <section class="card card--back">
    <div class="referral-panel"></div>
    <div class="gift-photo" role="img" aria-label="Rolled hundred-dollar bills tied with a red satin ribbon bow"></div>
    <svg class="ribbon" viewBox="0 0 371 426">
      <polygon points="127,0 211,0 0,196 0,111" fill="var(--brand-green)"/>
      <text x="85" y="91" transform="rotate(-45 85 82)" text-anchor="middle" fill="#fff"
        font-family="Poppins, sans-serif" font-weight="700" font-size="25">Refer a Friend</text>
    </svg>
    <div class="offer">
      <div class="offer__lead"><span class="offer__get">GET</span><span class="offer__upto">upto</span></div>
      <div class="offer__amount">$100</div>
    </div>
  </section>
</body>
</html>
```